MEDICAL CLINIC LETTERHEAD

Design is a letterhead for a non-profit medical center. The name of the clinic is VITORRANE Community Health Center. Although the full name must be included, the community health center part is more of a description and should be less visible - i attached an example of what I mean by that (ATTACHED IMAGE IS AN EXAMPLE OF FONT SIZES NOT A DESIGN IDEA). Please design something modern, cool looking and unique because I can always download free templates.
Phone, email, website and etc will be added later.

Industry/Entity Type

MEDICAL

```html
<!DOCTYPE html>
<html lang="en">
<head>
<meta charset="utf-8">
<title>VITORRANE Community Health Center – Letterhead</title>
<link href="https://fonts.googleapis.com/css2?family=Poppins:wght@400;500;600&family=Cormorant+Garamond:wght@500;600&family=Tinos&display=swap" rel="stylesheet">
<style>
  :root {
    --gold: #b09660;
    --navy: #1b2a4a;
    --ink: #3a3a3a;
    --paper: #ffffff;
    --backdrop: #e6e6e6;
  }
  * { margin: 0; padding: 0; box-sizing: border-box; }
  html, body { width: 1200px; height: 1200px; overflow: hidden; background: var(--backdrop); }
  .letterhead {
    position: absolute; left: 175px; top: 50px;
    width: 850px; height: 1100px;
    background: var(--paper);
    box-shadow: 0 6px 24px rgba(0,0,0,.12);
    font-family: "Poppins", sans-serif;
    color: var(--ink);
    overflow: hidden;
  }
  .side-name {
    position: absolute; left: 60px; top: 62px;
    display: flex; align-items: center; gap: 10px;
    font-family: "Poppins", sans-serif; font-weight: 600;
    font-size: 26px; letter-spacing: 1px; color: var(--navy);
  }
  .side-name .mark { width: 14px; height: 14px; background: var(--gold); }
  .brand { position: absolute; right: 60px; top: 48px; text-align: right; }
  .brand-name {
    font-family: "Cormorant Garamond", serif; font-weight: 600;
    font-size: 46px; letter-spacing: 1px; color: #111; line-height: 1;
  }
  .brand-tagline {
    font-size: 12.5px; letter-spacing: 1.2px; color: var(--gold);
    text-transform: uppercase; margin-top: 4px;
  }
  .date { position: absolute; right: 60px; top: 168px; font-size: 11px; color: var(--navy); font-weight: 500; }
  .date span { color: var(--gold); font-weight: 400; }
  .recipient { position: absolute; left: 60px; top: 250px; font-size: 12px; line-height: 1.55; color: #222; font-style: normal; }
  .recipient .name { color: var(--gold); font-weight: 600; font-size: 16px; }
  .letter-body {
    position: absolute; left: 60px; right: 60px; top: 360px;
    font-size: 11.5px; line-height: 1.9; color: #444;
  }
  .letter-body p { margin-bottom: 20px; }
  .contact {
    position: absolute; left: 60px; top: 850px;
    font-family: "Tinos", serif; font-size: 11.5px; color: #222;
  }
  .contact-row { display: flex; align-items: center; gap: 12px; margin-bottom: 9px; }
  .contact-icon {
    width: 20px; height: 20px; background: var(--gold);
    display: flex; align-items: center; justify-content: center; flex: none;
  }
  .contact-icon svg { width: 11px; height: 11px; }
  .contact-lines { line-height: 1.35; }
  .footer-swoosh { position: absolute; left: 0; bottom: 0; width: 850px; height: 220px; }
</style>
</head>
<body>
  <main class="letterhead">
    <div class="side-name"><span class="mark"></span>VITORRANE</div>

    <header class="brand">
      <div class="brand-name">VITORRANE</div>
      <div class="brand-tagline">Community Health Center</div>
    </header>

    <div class="date">Date: <span>19th October, 2023</span></div>

    <address class="recipient">
      To<br>
      <span class="name">Dana Whitlow</span><br>
      42 Linden Avenue, Harbor City<br>
      Westfield 48210
    </address>

    <section class="letter-body">
      <p>Lorem ipsum dolor sit amet, consectetur adipiscing elit. Integer et dignissim purus. Suspendisse dapibus diam maximus tempus iaculis. Nunc massa sapien, sodales non convallis in, feugiat et nisi. Pellentesque condimentum nisi vitae auctor sollicitudin. Ut faucibus tortor aliquam odio tristique, vitae vulputate leo laoreet. Integer cursus dignissim nisl eu interdum. Sed porttitor, urna sodales vestibulum viverra, mauris felis finibus purus, id sagittis sem ex mattis neque. Donec a nibh vitae orci tincidunt facilisis eu non dui.</p>
      <p>Nam varius mauris felis, a dignissim tortor ornare quis. Aliquam sit amet dapibus sem, at auctor orci. In non odio vestibulum, auctor orci et, condimentum nisl. Aenean tincidunt libero in ligula commodo eu tempus dui tincidunt. Phasellus sed iaculis lorem. Ut sit amet urna ligula. Quisque turpis risus, semper quis mauris eu, dictum vestibulum urna.</p>
      <p>Curabitur ac lacus et magna volutpat volutpat ut at turpis. Donec aliquet porta placerat. Pellentesque tincidunt, lacus nec rutrum faucibus, lectus erat tincidunt sem, quis vulputate erat ante quis sapien. Praesent sem elit, euismod eu fermentum a, vulputate sed dolor. Sed sed purus blandit, tempor felis vel, mattis risus. Etiam et quam cursus, placerat nulla in, semper elit. Curabitur enim leo, fringilla sit amet erat ut, lacinia vulputate metus. Ut libero diam, porttitor sit amet gravida vel, consequat in orci.</p>
    </section>

    <section class="contact">
      <div class="contact-row">
        <span class="contact-icon"><svg viewBox="0 0 12 12"><path d="M2 1l2 0 1 3-1.3 1a6 6 0 0 0 3.3 3.3L8 7l3 1v2a1 1 0 0 1-1 1A9 9 0 0 1 1 2a1 1 0 0 1 1-1z" fill="#fff"/></svg></span>
        <div class="contact-lines">(555) 014-2203<br>(555) 014-2271</div>
      </div>
      <div class="contact-row">
        <span class="contact-icon"><svg viewBox="0 0 12 12"><rect x="1" y="3" width="10" height="7" fill="#fff"/><path d="M1 3l5 4 5-4" stroke="#b09660" fill="none"/></svg></span>
        <div class="contact-lines">info@vitorrane.org</div>
      </div>
      <div class="contact-row">
        <span class="contact-icon"><svg viewBox="0 0 12 12"><circle cx="6" cy="6" r="4.5" stroke="#fff" fill="none"/><path d="M1.5 6h9M6 1.5c-2 2.5-2 6.5 0 9M6 1.5c2 2.5 2 6.5 0 9" stroke="#fff" fill="none" stroke-width=".8"/></svg></span>
        <div class="contact-lines">www.vitorrane.org</div>
      </div>
      <div class="contact-row">
        <span class="contact-icon"><svg viewBox="0 0 12 12"><path d="M6 11S2 6.8 2 4.5a4 4 0 0 1 8 0C10 6.8 6 11 6 11z" fill="#fff"/><circle cx="6" cy="4.5" r="1.4" fill="#b09660"/></svg></span>
        <div class="contact-lines">27 Elm Row, Riverton,<br>Westfield 31947</div>
      </div>
    </section>

    <svg class="footer-swoosh" viewBox="0 0 850 220" aria-hidden="true">
      <polygon points="0,220 0,212 470,150 590,70 700,45 850,5 850,22 720,62 600,86 480,166 40,220" fill="var(--gold)"/>
      <polyline points="0,206 465,144 585,62 696,38 850,-2" fill="none" stroke="var(--navy)" stroke-width="4"/>
    </svg>
  </main>
</body>
</html>
```